I am looking for help designing my new business cards. I would like rounded edges and a raised logo on the back of the card. I have 2 Logos. One with a boat in it and one without. I'd like the one on the back to be the one that includes the boat and just the name on the front. I have included multiple formats of my logo. Please let me know if you need anymore.

Target Market(s)

Potential buyers and other sales brokers

Industry/Entity Type

Sales - Yacht / Boat Sales

Contact Information for Business Card

Id liike the front to include just the business name portion of the logo along with my name (Corwin Dalby), phone number (555.318.6027), website address (www.dalbymarineco.example) and not my physical address but just "Marlow Bay, SC". The back should include my full logo that has the boat included. This portion I'd prefer raised amd take up the majority of the space there. Thanks!!

Colors
0054AA
0677BA
7BADD7
CADEEF
E8F1F8
0094D4
00A9DD
6FCCEA
C7EBF8
E9F6FB

Requirements
Must have
• Double sided
Nice to have
• My email address: Corwin@dalbymarineco.example The NMTG logo somewhere small on the front of the card
Should not have
• My full address, prefer only "Marlow Bay, SC"

```html
<!DOCTYPE html>
<html lang="en">
<head>
<meta charset="utf-8">
<title>Dalby Marine Co – Business Cards</title>
<link href="https://fonts.googleapis.com/css2?family=Montserrat:wght@400;500;700;800&display=swap" rel="stylesheet">
<style>
  :root{
    --stage:#b9b9b9;
    --navy:#1f2d5e;
    --edge:#1b87cf;
    --accent:#1e8fd6;
    --white:#ffffff;
    --rule:#8c97b8;
  }
  *{box-sizing:border-box;margin:0;padding:0}
  html,body{width:1200px;height:802px;overflow:hidden}
  body{
    background:var(--stage);
    font-family:"Montserrat",sans-serif;
    display:flex;align-items:center;justify-content:center;gap:40px;
  }
  .card{
    position:relative;width:560px;height:320px;
    background:var(--navy);border-radius:26px;
    border-bottom:4px solid var(--edge);
    box-shadow:0 14px 30px rgba(0,0,0,.28);
    color:var(--white);overflow:hidden;
  }
  /* front */
  .front .brand{
    position:absolute;left:40px;top:86px;
    font-weight:800;font-size:32px;line-height:1.05;letter-spacing:1px;
    color:var(--white);text-transform:uppercase;
  }
  .front .person{position:absolute;left:40px;top:208px}
  .person .name{color:var(--accent);font-weight:500;font-size:20px;letter-spacing:2px;text-transform:uppercase}
  .person .title{font-size:14px;margin-top:4px;text-align:right}
  .divider{position:absolute;left:280px;top:110px;width:1px;height:110px;background:var(--rule)}
  .contact{position:absolute;left:298px;top:110px;list-style:none}
  .contact li{display:flex;align-items:center;gap:8px;font-size:12.5px;margin-bottom:11px;white-space:nowrap}
  .contact svg{width:12px;height:12px;flex:none;fill:var(--accent)}
  .contact .mail{fill:none;stroke:var(--accent);stroke-width:2.5}
  .badge{position:absolute;right:28px;top:26px;width:46px;height:30px;border-radius:4px;background:var(--white)}
  /* back */
  .back{display:flex;flex-direction:column;align-items:center;justify-content:center;gap:14px}
  .back .illustration{
    width:300px;height:110px;border-radius:8px;
    background:linear-gradient(180deg,#2a3d78 0%,#1e6fb8 100%);
  }
  .back .brand{
    font-weight:800;font-size:40px;line-height:1.05;letter-spacing:2px;
    text-align:center;text-transform:uppercase;color:var(--white);
  }
</style>
</head>
<body>
  <section class="card front" aria-label="Card front">
    <div class="badge" role="img" aria-label="NMTG membership badge"></div>
    <div class="brand">Dalby<br>Marine Co</div>
    <div class="person">
      <p class="name">Corwin Dalby</p>
      <p class="title">Director</p>
    </div>
    <div class="divider"></div>
    <ul class="contact">
      <li><svg viewBox="0 0 24 24"><path d="M6.6 10.8a15 15 0 0 0 6.6 6.6l2.2-2.2a1 1 0 0 1 1-.25 11.4 11.4 0 0 0 3.6.6 1 1 0 0 1 1 1V20a1 1 0 0 1-1 1A17 17 0 0 1 3 4a1 1 0 0 1 1-1h3.5a1 1 0 0 1 1 1c0 1.25.2 2.45.6 3.6a1 1 0 0 1-.25 1z"/></svg>555.318.6027</li>
      <li><svg class="mail" viewBox="0 0 24 24"><path d="M3 6h18v12H3z M3 6l9 7 9-7"/></svg>Corwin@dalbymarineco.example</li>
      <li><svg viewBox="0 0 24 24"><circle cx="12" cy="12" r="10"/></svg>www.dalbymarineco.example</li>
      <li><svg viewBox="0 0 24 24"><path d="M12 2a7 7 0 0 0-7 7c0 5 7 13 7 13s7-8 7-13a7 7 0 0 0-7-7zm0 9.5A2.5 2.5 0 1 1 12 6.5a2.5 2.5 0 0 1 0 5z"/></svg>Marlow Bay, SC</li>
    </ul>
  </section>

  <section class="card back" aria-label="Card back">
    <div class="illustration" role="img" aria-label="Line drawing of a center-console boat riding a blue wave"></div>
    <div class="brand">Dalby<br>Marine Co</div>
  </section>
</body>
</html>
```